Landingpage Design X-Mas Invitation

Every year we invite customers to a special X-Mas Apéro. Since we are an IT-Company we handle the registration process by a landingpage. For this we need a design for the event 2016. The content will be the same as 2015 (you will finde the design attached from last year. There will be an additional job for creating the E-Mail.

Target Market(s)

Customers of IT Company, medium Companys in Central Switzerland

Industry/Entity Type

It Company

Number of Pages Required

1 page

Requirements
Must have
• Christmas Style

```html
<!DOCTYPE html>
<html lang="de">
<head>
<meta charset="utf-8">
<title>Lumeris Weihnachtsapéro – Anmeldung</title>
<link rel="stylesheet" href="https://fonts.googleapis.com/css2?family=Open+Sans:wght@400;600;700&family=Roboto:wght@400&family=Roboto+Condensed:wght@400;700&display=swap">
<style>
:root{
  --red-deep:#5c0306;
  --red-main:#a8080c;
  --red-bright:#c4100f;
  --form-bg:#c0412e;
  --form-border:#f0533a;
  --snow:#f4eaea;
  --snow-shade:#d69a9c;
  --dark:#2d2d2d;
  --btn:#383838;
  --white:#ffffff;
  --text-soft:#fbeaea;
  --badge:#c9c2c2;
  --tree:#3f6b1e;
  --tree-dark:#2c4f14;
}
*{box-sizing:border-box;margin:0;padding:0}
html,body{width:1200px;height:955px;overflow:hidden}
body{font-family:"Open Sans",sans-serif;background:var(--snow);position:relative}
.hero{position:absolute;left:0;top:0;width:1200px;height:793px;
  background:radial-gradient(ellipse at 42% 40%,var(--red-bright) 0%,var(--red-main) 40%,var(--red-deep) 100%);overflow:hidden}
.tree-art{position:absolute;left:69px;top:86px;width:518px;height:520px;
  background:radial-gradient(ellipse 50% 55% at 50% 58%,var(--tree) 0%,var(--tree-dark) 60%,rgba(44,79,20,0) 100%)}
.snow{position:absolute;left:0;top:0}
.event-note{position:absolute;color:var(--white);font-family:"Roboto Condensed",sans-serif;font-size:17px;line-height:18px;text-align:center;transform-origin:center}
.note-title{left:180px;top:120px;transform:rotate(-50deg)}
.note-date{left:410px;top:240px;transform:rotate(-50deg)}
.note-place{left:55px;top:360px;transform:rotate(-50deg)}
.brand{font-family:"Open Sans",sans-serif;font-weight:700;line-height:1;text-align:right}
.brand-name{display:block}
.brand-sub{display:block;font-weight:400;letter-spacing:1px}
.brand-hero{position:absolute;left:754px;top:52px;color:var(--white)}
.brand-hero .brand-name{font-size:48px}
.brand-hero .brand-sub{font-size:13px;margin-top:2px}
.brand-tree{position:absolute;left:270px;top:646px;color:#c3392b}
.brand-tree .brand-name{font-size:27px}
.brand-tree .brand-sub{font-size:7px;color:#555}
.intro{position:absolute;left:574px;top:128px;width:575px;color:var(--text-soft);font-family:"Roboto",sans-serif;font-size:13px;line-height:26px;text-align:center}
.signup{position:absolute;left:591px;top:232px;width:546px;height:268px;background:var(--form-bg);border:2px solid var(--form-border);border-radius:3px}
.signup h2{position:absolute;top:30px;color:var(--white);font-family:"Roboto Condensed",sans-serif;font-weight:700;font-size:21px}
.col-self{left:22px}.col-guest{left:278px}
.field{position:absolute;width:245px;height:37px;background:var(--white);border:1px solid #ddd;font-family:"Open Sans",sans-serif;font-size:11.5px;color:#666;padding:0 11px;line-height:35px}
.actions .btn{position:absolute;top:208px;height:36px;background:var(--btn);color:var(--white);font-family:"Roboto Condensed",sans-serif;font-size:15px;border:none;border-radius:2px;line-height:36px;text-align:center}
.partners{position:absolute;left:0;top:730px;width:1200px;display:flex;justify-content:center;gap:18px;align-items:center}
.partner{height:26px;background:var(--badge);border-radius:4px}
.footer{position:absolute;left:0;top:793px;width:1200px;height:162px;background:var(--dark);color:var(--white)}
.brand-foot{position:absolute;left:97px;top:26px}
.brand-foot .brand-name{font-size:38px}
.brand-foot .brand-sub{font-size:11px}
.contact{position:absolute;top:30px;display:flex;gap:12px;font-size:13px;line-height:21px}
.contact svg{flex:none}
.contact strong{font-weight:600;font-size:14px}
.c-address{left:352px;width:320px}
.c-phone{left:712px}
.c-mail{left:922px}
.rule{position:absolute;left:0;top:100px;width:1200px;height:1px;background:#444}
.copyright{position:absolute;left:0;top:126px;width:1200px;text-align:center;font-family:"Roboto",sans-serif;font-size:13px}
</style>
</head>
<body>
<section class="hero">
  <div class="tree-art" role="img" aria-label="Illustrierter Weihnachtsbaum mit Stern, Kerzen, Kugeln, Lichterkette und Geschenken"></div>
  <svg class="snow" width="1200" height="793" viewBox="0 0 1200 793" aria-hidden="true">
    <path d="M0 590 C180 560 330 630 520 600 C700 565 900 540 1200 600 L1200 793 L0 793Z" fill="var(--snow-shade)"/>
    <path d="M0 640 C220 600 420 690 640 640 C840 600 1000 660 1200 620 L1200 793 L0 793Z" fill="var(--snow)"/>
  </svg>
  <p class="event-note note-title">Lumeris<br>Weihnachts<br>apéro</p>
  <p class="event-note note-date">17. Dezember 2015<br>17 - 20 Uhr</p>
  <p class="event-note note-place">Sternlounge<br>Tannenweg 12<br>Luzern</p>
  <div class="brand brand-tree"><span class="brand-name">Lumeris</span><span class="brand-sub">IT SOLUTIONS</span></div>

  <div class="brand brand-hero"><span class="brand-name">Lumeris</span><span class="brand-sub">IT SOLUTIONS</span></div>
  <p class="intro">Ob Sie den ganzen Abend bleiben oder nur kurz nach dem Weihnachts-Shopping vorbeischauen, ist ganz Ihnen überlassen. Wir freuen uns sehr, wenn Sie uns die Gelegenheit geben, Ihnen mit dieser Einladung für die erfolgreiche Zusammenarbeit herzlichst zu danken.</p>

  <form class="signup">
    <h2 class="col-self">IHRE ANMELDUNG</h2>
    <h2 class="col-guest">IHRE BEGLEITPERSON</h2>
    <div class="field" style="left:24px;top:69px">Ihre E-Mail-Adresse</div>
    <div class="field" style="left:24px;top:109px">Vorname</div>
    <div class="field" style="left:24px;top:149px">Nachname</div>
    <div class="field" style="left:280px;top:69px">Vorname</div>
    <div class="field" style="left:280px;top:109px">Nachname</div>
    <div class="field" style="left:280px;top:149px">Firma (Optional)</div>
    <div class="actions">
      <span class="btn" style="left:133px;width:173px">WEITERE BEGLEITPERSON</span>
      <span class="btn" style="left:313px;width:87px">ABSENDEN</span>
    </div>
  </form>

  <div class="partners" aria-label="Partner">
    <span class="partner" style="width:38px;border-radius:50%;height:38px"></span>
    <span class="partner" style="width:120px"></span>
    <span class="partner" style="width:62px"></span>
    <span class="partner" style="width:46px"></span>
    <span class="partner" style="width:122px"></span>
    <span class="partner" style="width:80px"></span>
    <span class="partner" style="width:66px"></span>
    <span class="partner" style="width:90px"></span>
    <span class="partner" style="width:56px"></span>
    <span class="partner" style="width:64px"></span>
    <span class="partner" style="width:108px"></span>
  </div>
</section>

<footer class="footer">
  <div class="brand brand-foot"><span class="brand-name">Lumeris</span><span class="brand-sub">IT SOLUTIONS</span></div>
  <div class="contact c-address">
    <svg width="34" height="34" viewBox="0 0 34 34" aria-hidden="true"><circle cx="17" cy="17" r="16" fill="none" stroke="#fff" stroke-width="1.3"/><path d="M17 9a5 5 0 0 0-5 5c0 4 5 10 5 10s5-6 5-10a5 5 0 0 0-5-5z" fill="#fff"/><circle cx="17" cy="14" r="2" fill="var(--dark)"/></svg>
    <span>KONTAKT :&nbsp;&nbsp; Lumeris IT Solutions AG Tannenweg 12 6004 Luzern</span>
  </div>
  <div class="contact c-phone">
    <svg width="34" height="34" viewBox="0 0 34 34" aria-hidden="true"><circle cx="17" cy="17" r="16" fill="none" stroke="#fff" stroke-width="1.3"/><path d="M12 10c1-1 2 0 3 2s0 2-1 3c1 2 3 4 5 5 1-1 1-2 3-1s3 2 2 3c-2 3-6 2-9-1s-5-8-3-11z" fill="#fff"/></svg>
    <span>Telefon:<br><strong>041 555 01 20</strong></span>
  </div>
  <div class="contact c-mail">
    <svg width="34" height="34" viewBox="0 0 34 34" aria-hidden="true"><circle cx="17" cy="17" r="16" fill="none" stroke="#fff" stroke-width="1.3"/><path d="M17 9a5 5 0 0 0-5 5c0 4 5 10 5 10s5-6 5-10a5 5 0 0 0-5-5z" fill="#fff"/><circle cx="17" cy="14" r="2" fill="var(--dark)"/></svg>
    <span>Email:<br>info@lumeris-it.ch</span>
  </div>
  <div class="rule"></div>
  <p class="copyright">© Copyright 2016 Lumeris . All Rights Reserved.</p>
</footer>
</body>
</html>
```